Business Card Design Project

We need a logo design for a new company based in Southern California called "Norvale Security Services, Inc." We install security and camera systems for homeowners and business, to protect their assets.
Updates

Project Deadline Extended
Reason: LOGO Design completes in eight days. Would like that design decided before we finish the business cards. Thanks...

Target Market(s)

Homeowners and business owners looking for additional protection of their assets.

Industry/Entity Type

Security

Font styles to use
Serif

Requirements
Must have
• Company Name
Office# 909-472-3615
Service# 909-472-3616
email: NorvaleSecurity@brimwell.net
address: 48620 Thorncrest Lane Ashcombe Hills, CA 91704
Nice to have
• Serving Southern California

```html
<!DOCTYPE html>
<html lang="en">
<head>
<meta charset="utf-8">
<title>Norvale Security Services, Inc. — Business Card</title>
<link rel="stylesheet" href="https://fonts.googleapis.com/css2?family=Open+Sans:wght@400;700&display=swap">
<style>
  :root {
    --canvas: #e9e9e9;
    --card: #ffffff;
    --ink: #111111;
    --band: #1b1b1b;
    --on-band: #ffffff;
    --divider: #ffffff;
  }
  * { box-sizing: border-box; margin: 0; padding: 0; }
  html, body {
    width: 1200px;
    height: 1000px;
    overflow: hidden;
    background: var(--canvas);
    font-family: "Open Sans", sans-serif;
  }
  .business-card {
    position: absolute;
    left: 340px;
    top: 70px;
    width: 520px;
    height: 860px;
    background: var(--card);
    box-shadow: 0 10px 30px rgba(0,0,0,0.18);
    overflow: hidden;
  }
  .top-rule {
    position: absolute;
    top: 78px;
    left: 70px;
    width: 420px;
    height: 4px;
    background: var(--ink);
  }
  .brand {
    position: absolute;
    top: 250px;
    left: 0;
    width: 100%;
    display: flex;
    align-items: center;
    justify-content: center;
    gap: 12px;
  }
  .brand-mark {
    width: 18px;
    height: 18px;
    border-radius: 50%;
    background: var(--ink);
  }
  .brand-name {
    font-weight: 700;
    font-size: 27px;
    color: var(--ink);
    letter-spacing: 0.2px;
    white-space: nowrap;
  }
  .contact-band {
    position: absolute;
    top: 470px;
    left: 0;
    width: 100%;
    height: 300px;
    background: var(--band);
    color: var(--on-band);
  }
  .contact-row {
    display: flex;
    align-items: center;
    gap: 28px;
    padding: 0 20px 0 44px;
    height: 100px;
    font-size: 19px;
    line-height: 1.3;
    border-bottom: 3px solid var(--divider);
  }
  .contact-row:last-child { border-bottom: none; }
  .contact-icon {
    width: 34px;
    height: 34px;
    flex: none;
  }
  .contact-text { white-space: nowrap; }
  .service-area {
    position: absolute;
    top: 770px;
    left: 0;
    width: 100%;
    height: 90px;
    display: flex;
    align-items: center;
    justify-content: center;
    font-size: 19px;
    color: var(--ink);
  }
</style>
</head>
<body>
  <main class="business-card">
    <div class="top-rule"></div>

    <div class="brand">
      <span class="brand-mark"></span>
      <span class="brand-name">Norvale Security Services, Inc.</span>
    </div>

    <section class="contact-band">
      <div class="contact-row">
        <svg class="contact-icon" viewBox="0 0 34 34" aria-hidden="true">
          <path d="M4 11c0-4 6-6 13-6s13 2 13 6v3h-7v-3c-2-1-10-1-12 0v3H4z" fill="#fff"/>
          <path d="M9 15h16l4 13H5z" fill="#fff"/>
          <circle cx="17" cy="21" r="3.5" fill="#1b1b1b"/>
        </svg>
        <div class="contact-text">
          Office : + 909-472-3615<br>
          Service: + 909-472-3616
        </div>
      </div>
      <div class="contact-row">
        <svg class="contact-icon" viewBox="0 0 34 34" aria-hidden="true" fill="none" stroke="#fff" stroke-width="2">
          <circle cx="17" cy="17" r="14"/>
          <ellipse cx="17" cy="17" rx="6" ry="14"/>
          <line x1="3" y1="17" x2="31" y2="17"/>
          <path d="M6 9h22M6 25h22"/>
        </svg>
        <div class="contact-text">NorvaleSecurity@brimwell.net</div>
      </div>
      <div class="contact-row">
        <svg class="contact-icon" viewBox="0 0 34 34" aria-hidden="true">
          <path d="M17 2c-6 0-10 4.5-10 10 0 7.5 10 20 10 20s10-12.5 10-20c0-5.5-4-10-10-10z" fill="#fff"/>
          <circle cx="17" cy="12" r="4" fill="#1b1b1b"/>
        </svg>
        <div class="contact-text">
          48620 Thorncrest Lane Ashcombe Hills<br>
          CA 91704
        </div>
      </div>
    </section>

    <footer class="service-area">Serving Southern California</footer>
  </main>
</body>
</html>
```